Information Security Company Business Cards

Using our included logo, we need a business card design. It should have standard contact information such as :

Ravi Tanner
Senior Security Engineer
ravi.tanner@quorvex-hub.com
877.640.3958

Maybe include the website "www.quorvex-hub.com" that we will be redesigning soon.??

open to suggestions of course...

Target Market(s)

Our customers are small to large companies. Generally health-care, financial, insurance and the like.

Industry/Entity Type

Business

Font styles to use
Other font styles liked:
• Something that works with the logo

Requirements
Must have
• Colors should flow with the logo if possible. Or at least we think it should.

```html
<!DOCTYPE html>
<html lang="en">
<head>
<meta charset="utf-8">
<title>Quorvex Hub Business Cards</title>
<link href="https://fonts.googleapis.com/css2?family=Arimo:wght@400;700&display=swap" rel="stylesheet">
<style>
  :root {
    --page-bg: #e6e6e8;
    --card-bg: #f4f3f1;
    --brand-blue: #2a2de0;
    --ink-dark: #2b2b2b;
    --ink-mid: #555555;
    --stripe-dark: #333333;
  }
  * { margin: 0; padding: 0; box-sizing: border-box; }
  html, body {
    width: 1200px; height: 1000px; overflow: hidden;
    background: var(--page-bg);
    font-family: "Arimo", Arial, sans-serif;
  }
  .card {
    position: absolute; left: 250px;
    width: 700px; height: 400px;
    background: linear-gradient(135deg, #ffffff 0%, var(--card-bg) 60%, #e9e7e3 100%);
    box-shadow: 0 6px 18px rgba(0,0,0,0.18);
    overflow: hidden;
  }
  .card--front { top: 60px; }
  .card--back { top: 540px; }

  .fold-shadow {
    position: absolute; left: 0; top: 0; width: 100%; height: 100%;
  }

  .brand {
    position: absolute; display: flex; align-items: center;
  }
  .brand__dot {
    border-radius: 50%; border: 10px solid var(--brand-blue);
  }
  .brand__name {
    color: var(--brand-blue); font-weight: 700; text-transform: uppercase;
    letter-spacing: 1px;
  }
  .card--front .brand { left: 150px; top: 110px; gap: 22px; }
  .card--front .brand__dot { width: 110px; height: 110px; }
  .card--front .brand__name { font-size: 50px; line-height: 1; }

  .front__site {
    position: absolute; left: 0; right: 0; top: 292px;
    text-align: center; font-size: 34px; font-weight: 700; color: var(--ink-dark);
  }

  .card--back .brand { left: 40px; top: 36px; gap: 12px; }
  .card--back .brand__dot { width: 52px; height: 52px; border-width: 6px; }
  .card--back .brand__name { font-size: 22px; }

  .contact {
    position: absolute; right: 40px; top: 110px; text-align: right; color: var(--ink-dark);
  }
  .contact__name { font-size: 30px; font-weight: 700; }
  .contact__title { font-size: 18px; color: var(--ink-mid); margin-top: 4px; }
  .contact__email { font-size: 22px; margin-top: 14px; }
  .contact__phone { font-size: 26px; margin-top: 6px; }

  .site-band {
    position: absolute; left: 0; bottom: 0; width: 100%; height: 66px;
  }
  .site-band__text {
    position: absolute; left: 30px; bottom: 16px;
    font-size: 30px; color: #ffffff; font-weight: 400;
  }
</style>
</head>
<body>
  <section class="card card--front">
    <svg class="fold-shadow" viewBox="0 0 700 400" aria-hidden="true">
      <defs>
        <linearGradient id="frontFold" x1="0" y1="0" x2="0" y2="1">
          <stop offset="0" stop-color="#000" stop-opacity="0"/>
          <stop offset="1" stop-color="#000" stop-opacity="0.08"/>
        </linearGradient>
      </defs>
      <path d="M60 270 Q350 240 640 270 L640 285 Q350 255 60 285 Z" fill="url(#frontFold)"/>
    </svg>
    <div class="brand">
      <span class="brand__dot"></span>
      <span class="brand__name">Quorvex Hub</span>
    </div>
    <p class="front__site">www.quorvex-hub.com</p>
  </section>

  <section class="card card--back">
    <div class="brand">
      <span class="brand__dot"></span>
      <span class="brand__name">Quorvex Hub</span>
    </div>
    <div class="contact">
      <p class="contact__name">Ravi Tanner</p>
      <p class="contact__title">Senior Security Engineer</p>
      <p class="contact__email">ravi.tanner@quorvex-hub.com</p>
      <p class="contact__phone">877.640.3958</p>
    </div>
    <svg class="site-band" viewBox="0 0 700 66" preserveAspectRatio="none" aria-hidden="true">
      <rect x="0" y="0" width="480" height="66" fill="var(--brand-blue)"/>
      <polygon points="480,0 700,0 700,66 480,66" fill="var(--stripe-dark)"/>
      <g fill="var(--card-bg)">
        <polygon points="510,0 520,0 500,66 490,66"/>
        <polygon points="545,0 555,0 535,66 525,66"/>
        <polygon points="580,0 590,0 570,66 560,66"/>
        <polygon points="615,0 625,0 605,66 595,66"/>
        <polygon points="650,0 700,0 700,66 630,66"/>
      </g>
    </svg>
    <p class="site-band__text">www.quorvex-hub.com</p>
  </section>
</body>
</html>
```